Bref créative
Dentwise Business Cards and Stationery
Paintless Dent Repair
Modern
Calvin t Moss
Owner-Technician
4172 Salvia ln
lakemont ca 91734
glowmenderfxk7@mailvista.example
repair dings dents hail damage
20 years experience master craftsman

```html
<!DOCTYPE html>
<html lang="en">
<head>
<meta charset="utf-8">
<title>Dentwise Business Cards</title>
<link href="https://fonts.googleapis.com/css2?family=Open+Sans:wght@400;600;700&display=swap" rel="stylesheet">
<style>
  :root {
    --bg: #e9e9e9;
    --card: #ffffff;
    --red: #d31f26;
    --red-dark: #a4141a;
    --ink: #3a3a3a;
    --muted: #8a8a8a;
  }
  * { margin: 0; padding: 0; box-sizing: border-box; }
  html, body { width: 1200px; height: 874px; overflow: hidden; }
  body {
    background: var(--bg);
    font-family: "Open Sans", Arial, sans-serif;
    position: relative;
  }
  .card {
    position: absolute;
    width: 500px;
    height: 286px;
    background: var(--card);
    border-radius: 22px;
    overflow: hidden;
    box-shadow: 0 10px 28px rgba(0,0,0,0.18);
  }
  .card--front { left: 60px; top: 294px; }
  .card--back { left: 640px; top: 294px; }

  .card__wave { position: absolute; inset: 0; width: 100%; height: 100%; }

  .brand {
    position: absolute;
    left: 0; right: 0;
    text-align: center;
  }
  .brand__name {
    font-family: "Open Sans", Arial, sans-serif;
    font-weight: 700;
    color: var(--red);
    font-size: 42px;
    line-height: 1;
  }
  .brand__tagline {
    margin-top: 8px;
    color: var(--ink);
    font-size: 14px;
    font-weight: 700;
    letter-spacing: 2px;
  }
  .card--front .brand { top: 36px; }
  .card--back .brand { top: 66px; }

  .contact {
    position: absolute;
    left: 26px;
    bottom: 22px;
    list-style: none;
    color: #fff;
    font-size: 11px;
    line-height: 1.55;
  }
  .contact__item { display: flex; align-items: center; gap: 7px; }
  .contact__icon {
    width: 13px; height: 13px;
    background: #fff;
    border-radius: 50%;
    display: inline-flex; align-items: center; justify-content: center;
    flex: none;
  }
  .contact__address { padding-left: 20px; }

  .person {
    position: absolute;
    right: 30px;
    top: 160px;
    color: #fff;
    text-align: left;
  }
  .person__name { font-size: 15px; font-weight: 600; }
  .person__role { font-size: 12px; }

  .back__note {
    position: absolute;
    top: 146px; left: 0; right: 0;
    text-align: center;
    color: var(--muted);
    font-size: 10px;
    letter-spacing: 0.5px;
  }
  .back__web {
    position: absolute;
    bottom: 40px; left: 0; right: 0;
    text-align: center;
    color: var(--red);
    font-size: 14px;
    letter-spacing: 1px;
  }
</style>
</head>
<body>

  <section class="card card--front" aria-label="Business card front">
    <svg class="card__wave" viewBox="0 0 500 286" preserveAspectRatio="none" aria-hidden="true">
      <path d="M0 142 C140 122 300 160 500 118 L500 286 L0 286 Z" fill="var(--red-dark)"/>
      <path d="M0 156 C150 138 310 176 500 132 L500 286 L0 286 Z" fill="var(--red)"/>
    </svg>
    <div class="brand">
      <div class="brand__name">Dentwise</div>
      <div class="brand__tagline">Paintless dent repair</div>
    </div>
    <div class="person">
      <div class="person__name">Calvin t Moss</div>
      <div class="person__role">Owner-Technician</div>
    </div>
    <ul class="contact">
      <li class="contact__item">
        <span class="contact__icon"><svg width="9" height="9" viewBox="0 0 10 10"><path d="M5 0.5a3 3 0 0 1 3 3c0 2.3-3 6-3 6s-3-3.7-3-6a3 3 0 0 1 3-3z" fill="var(--red)"/></svg></span>
        4172 Salvia ln
      </li>
      <li class="contact__address">lakemont ca 91734</li>
      <li class="contact__item">
        <span class="contact__icon"><svg width="9" height="9" viewBox="0 0 10 10"><path d="M2 1h2l1 2.5-1.2 1a5 5 0 0 0 2.7 2.7l1-1.2L10 7v2a1 1 0 0 1-1 1A8 8 0 0 1 1 2a1 1 0 0 1 1-1z" fill="var(--red)"/></svg></span>
        628-555-0142
      </li>
      <li class="contact__item">
        <span class="contact__icon"><svg width="9" height="9" viewBox="0 0 10 10"><rect x="1" y="2.5" width="8" height="5.5" fill="var(--red)"/><path d="M1 2.5l4 3 4-3" stroke="#fff" stroke-width="0.8" fill="none"/></svg></span>
        glowmenderfxk7@mailvista.example
      </li>
      <li class="contact__item">
        <span class="contact__icon"><svg width="9" height="9" viewBox="0 0 10 10"><circle cx="5" cy="5" r="4" fill="none" stroke="var(--red)" stroke-width="1"/><path d="M1 5h8M5 1c-2 2.5-2 5.5 0 8M5 1c2 2.5 2 5.5 0 8" stroke="var(--red)" stroke-width="0.8" fill="none"/></svg></span>
        www.dentwise-repair.example
      </li>
    </ul>
  </section>

  <section class="card card--back" aria-label="Business card back">
    <div class="brand">
      <div class="brand__name">Dentwise</div>
      <div class="brand__tagline">Paintless dent repair</div>
    </div>
    <p class="back__note">repair dings dents hail damage</p>
    <p class="back__web">www.dentwise-repair.example</p>
  </section>

</body>
</html>
```